3 out of 100 people will get deadly skin cancer - we need a great illustration that shows this!

We put together a prototype image that communicates lifetime skin cancer risk. (see attached). We are looking for illustrators who can take make a new/better/cooler graphic that communicates this idea. It could be as simple as a superior illustration of the graphic we have or illustrators can propose a completely different idea.What should the illustration communicate?U.S. adults have a lifetime risk of developing skin cancer of 1 in 5. But we don't want to show 1 in 5; we want to show that number in a larger group. For example, in the attached illustration we show 20 in 100 people get skin cancer (i.e., 100 beach towels/umbrellas and 20 of them are red). Research has shown that people are more likely to accurately understand numbers like this when you convey them for larger groups (i.e., 20 out of 100 rather than 1 out of 5). U.S. adults also have a lifetime risk of 2.3% of developing the deadliest form of skin cancer (melanoma). In other words, approximately 3 in 100 people will develop melanoma in their lifetime. Ideally, a single image will convey both lifetime skin cancer risk (20 in 100) and melanoma risk (3 in 100). We will award a top three as follows: 1st place = $300, 2nd place = $250, third place = $200. We will also buy any design beyond 3rd place that we like for $100. For example, we purchased 24 designs in our last contest on Artmarketly.This research is supported by funding from the Corvane Institute of Science.

Target Market(s)

The U.S. public; individuals at high risk of developing skin cancer

Industry/Entity Type

Medicine

Colors

Designer to choose colors to be used in the design.

Requirements
Must have
• an original illustration that conveys both lifetime risk of developing skin cancer (20 in 100) and melanoma (3 in 100).
Nice to have
• It can be beach towels and umbrellas, just like our prototype, or the designers can pitch an original idea. Imagery can be realistic or cartoonish (or something in between). It should be illustrations, though. Not edited photos. The image should be in color (no black and white illustrations).
Should not have
• Photos. Clip art. Free vector images.
• We are looking for original illustrations created by the designer.

```html
<!DOCTYPE html>
<html lang="en">
<head>
<meta charset="utf-8">
<title>Skin Cancer – Lifetime Risk</title>
<link rel="stylesheet" href="https://fonts.googleapis.com/css2?family=Noto+Sans:wght@600;700;800&display=swap">
<style>
  :root {
    --sand: #fddc8a;
    --sand-light: #fde8ae;
    --sand-pale: #fef0c8;
    --sun: #f8ac3c;
    --sea: #83d2f4;
    --sea-light: #bfeafa;
    --foam: #ffffff;
    --ink: #111111;
    --orange: #f7941d;
    --orange-light: #f6b46a;
    --blue: #1b75bb;
    --blue-light: #8ed3f3;
    --red: #b1232b;
    --red-light: #d4555b;
  }
  * { margin: 0; padding: 0; box-sizing: border-box; }
  html, body { width: 853px; height: 1200px; overflow: hidden; background: var(--sand); }
  .poster {
    position: relative; width: 853px; height: 1200px; overflow: hidden;
    background: var(--sand);
    font-family: "Noto Sans", Arial, sans-serif; color: var(--ink);
  }
  .backdrop { position: absolute; inset: 0; }
  .title {
    position: absolute; top: 44px; left: 0; width: 853px; text-align: center;
    font-size: 73px; font-weight: 800; color: var(--orange); letter-spacing: 1px; line-height: 1;
  }
  .fact {
    position: absolute; font-size: 29px; font-weight: 700; line-height: 35px;
  }
  .fact--cause { left: 47px; top: 142px; width: 370px; }
  .fact--exposure { left: 446px; top: 164px; width: 400px; }
  .question {
    position: absolute; left: 47px; top: 360px; font-size: 36px; font-weight: 700; line-height: 42px;
  }
  .question__lead { display: block; font-size: 25px; line-height: 28px; }
  .prompt {
    position: absolute; left: 125px; top: 458px; width: 640px;
    font-size: 26px; font-weight: 700; line-height: 35px;
  }
  .prompt .is-cancer { color: var(--orange); }
  .prompt .is-melanoma { color: var(--red); }
  .grid {
    position: absolute; left: 64px; top: 606px;
    display: grid; grid-template-columns: repeat(10, 46.8px); grid-auto-rows: 46px;
  }
  .grid svg, .legend svg { width: 42px; height: 42px; display: block; }
  .clear { --tone-a: var(--blue-light); --tone-b: var(--blue); }
  .cancer { --tone-a: var(--orange-light); --tone-b: var(--orange); }
  .melanoma { --tone-a: var(--red-light); --tone-b: var(--red); }
  .legend { position: absolute; left: 560px; top: 736px; list-style: none; }
  .legend li { display: flex; align-items: center; height: 58px; font-size: 20px; font-weight: 700; }
  .legend svg { margin-right: 20px; }
  .legend .clear { color: var(--blue); }
  .legend .cancer { color: var(--orange); }
  .legend .melanoma { color: var(--red); }
  .prevent {
    position: absolute; left: 0; top: 1092px; width: 853px; height: 50px;
    background: var(--sand-pale); padding-left: 47px;
    font-size: 36px; font-weight: 700; line-height: 50px;
  }
  .more { position: absolute; left: 47px; top: 1150px; font-size: 22px; font-weight: 700; }
</style>
</head>
<body>
<main class="poster">
  <svg class="backdrop" width="853" height="1200" viewBox="0 0 853 1200" aria-hidden="true">
    <path d="M330 0 C430 60 520 140 560 240 L600 240 C560 120 470 40 420 0 Z" fill="var(--sand-light)"/>
    <path d="M470 0 C600 70 680 200 700 420 C690 250 620 110 560 0 Z" fill="var(--sand-light)"/>
    <path d="M620 0 C700 60 760 120 800 200 C760 90 720 40 690 0 Z" fill="var(--sand-light)"/>
    <circle cx="870" cy="330" r="210" fill="var(--sun)"/>
    <path d="M0 420 C200 380 400 390 560 360 C680 340 780 330 853 330 L853 800 C700 640 420 560 0 545 Z" fill="var(--sea)"/>
    <path d="M0 460 C220 440 420 470 600 470 C720 470 800 480 853 490 L853 790 C700 650 420 580 0 540 Z" fill="var(--sea-light)" opacity="0.7"/>
    <path d="M0 540 C420 580 700 640 853 790 L853 830 C700 690 420 610 0 575 Z" fill="var(--foam)"/>
    <path d="M0 575 C420 610 700 690 853 830 L853 845 C700 710 420 630 0 590 Z" fill="var(--sea-light)"/>
    <path d="M0 590 C420 630 700 710 853 845 L853 1000 C760 860 560 720 0 680 Z" fill="var(--sand-light)" opacity="0.6"/>
    <path d="M0 680 C560 720 760 860 853 1000 L853 1060 C760 920 560 760 0 720 Z" fill="var(--sand-light)" opacity="0.5"/>
    <defs>
      <symbol id="beach-spot" viewBox="0 0 64 64">
        <path d="M10 28 A24 22 0 0 1 58 28 Z" fill="var(--tone-a)"/>
        <path d="M34 6 C26 10 22 18 22 28 L30 28 C30 18 32 11 34 6 Z" fill="var(--tone-b)"/>
        <path d="M34 6 C44 10 50 18 50 28 L42 28 C42 18 38 11 34 6 Z" fill="var(--tone-b)"/>
        <line x1="34" y1="28" x2="30" y2="60" stroke="var(--tone-a)" stroke-width="3"/>
        <path d="M4 34 L16 46 L56 46 L56 52 L14 52 L2 38 Z" fill="var(--tone-b)"/>
        <line x1="18" y1="52" x2="12" y2="62" stroke="var(--tone-b)" stroke-width="4"/>
        <line x1="50" y1="52" x2="56" y2="62" stroke="var(--tone-b)" stroke-width="4"/>
      </symbol>
    </defs>
  </svg>

  <h1 class="title">SKIN CANCER</h1>
  <p class="fact fact--cause">The primary cause of skin cancer is exposure to ultraviolet (UV) light from the sun or indoor tanning.</p>
  <p class="fact fact--exposure">The greater the total amount of sun exposure over lifetime, the greater the chance of melanoma.</p>

  <h2 class="question">How likely are you to get skin cancer?<span class="question__lead">Let’s say 100 people go to the beach...</span></h2>
  <p class="prompt">How many will develop <span class="is-cancer">skin cancer</span> in their lifetime? How many will develop <span class="is-melanoma">melanoma</span>, the deadliest form of skin cancer?</p>

  <div class="grid" role="img" aria-label="100 beach spots: 20 with skin cancer, 3 with melanoma, 77 with no skin cancer">
    <!-- row 1 -->
    <svg class="clear"><use href="#beach-spot"/></svg><svg class="cancer"><use href="#beach-spot"/></svg><svg class="clear"><use href="#beach-spot"/></svg><svg class="clear"><use href="#beach-spot"/></svg><svg class="clear"><use href="#beach-spot"/></svg><svg class="cancer"><use href="#beach-spot"/></svg><svg class="clear"><use href="#beach-spot"/></svg><svg class="clear"><use href="#beach-spot"/></svg><svg class="clear"><use href="#beach-spot"/></svg><svg class="clear"><use href="#beach-spot"/></svg>
    <!-- row 2 -->
    <svg class="clear"><use href="#beach-spot"/></svg><svg class="clear"><use href="#beach-spot"/></svg><svg class="cancer"><use href="#beach-spot"/></svg><svg class="clear"><use href="#beach-spot"/></svg><svg class="cancer"><use href="#beach-spot"/></svg><svg class="clear"><use href="#beach-spot"/></svg><svg class="clear"><use href="#beach-spot"/></svg><svg class="clear"><use href="#beach-spot"/></svg><svg class="cancer"><use href="#beach-spot"/></svg><svg class="clear"><use href="#beach-spot"/></svg>
    <!-- row 3 -->
    <svg class="cancer"><use href="#beach-spot"/></svg><svg class="clear"><use href="#beach-spot"/></svg><svg class="clear"><use href="#beach-spot"/></svg><svg class="clear"><use href="#beach-spot"/></svg><svg class="clear"><use href="#beach-spot"/></svg><svg class="clear"><use href="#beach-spot"/></svg><svg class="clear"><use href="#beach-spot"/></svg><svg class="cancer"><use href="#beach-spot"/></svg><svg class="clear"><use href="#beach-spot"/></svg><svg class="clear"><use href="#beach-spot"/></svg>
    <!-- row 4 -->
    <svg class="clear"><use href="#beach-spot"/></svg><svg class="cancer"><use href="#beach-spot"/></svg><svg class="cancer"><use href="#beach-spot"/></svg><svg class="clear"><use href="#beach-spot"/></svg><svg class="clear"><use href="#beach-spot"/></svg><svg class="melanoma"><use href="#beach-spot"/></svg><svg class="clear"><use href="#beach-spot"/></svg><svg class="clear"><use href="#beach-spot"/></svg><svg class="clear"><use href="#beach-spot"/></svg><svg class="clear"><use href="#beach-spot"/></svg>
    <!-- row 5 -->
    <svg class="clear"><use href="#beach-spot"/></svg><svg class="clear"><use href="#beach-spot"/></svg><svg class="clear"><use href="#beach-spot"/></svg><svg class="clear"><use href="#beach-spot"/></svg><svg class="clear"><use href="#beach-spot"/></svg><svg class="clear"><use href="#beach-spot"/></svg><svg class="cancer"><use href="#beach-spot"/></svg><svg class="clear"><use href="#beach-spot"/></svg><svg class="clear"><use href="#beach-spot"/></svg><svg class="clear"><use href="#beach-spot"/></svg>
    <!-- row 6 -->
    <svg class="clear"><use href="#beach-spot"/></svg><svg class="melanoma"><use href="#beach-spot"/></svg><svg class="clear"><use href="#beach-spot"/></svg><svg class="clear"><use href="#beach-spot"/></svg><svg class="cancer"><use href="#beach-spot"/></svg><svg class="clear"><use href="#beach-spot"/></svg><svg class="clear"><use href="#beach-spot"/></svg><svg class="clear"><use href="#beach-spot"/></svg><svg class="clear"><use href="#beach-spot"/></svg><svg class="cancer"><use href="#beach-spot"/></svg>
    <!-- row 7 -->
    <svg class="clear"><use href="#beach-spot"/></svg><svg class="cancer"><use href="#beach-spot"/></svg><svg class="clear"><use href="#beach-spot"/></svg><svg class="clear"><use href="#beach-spot"/></svg><svg class="clear"><use href="#beach-spot"/></svg><svg class="clear"><use href="#beach-spot"/></svg><svg class="cancer"><use href="#beach-spot"/></svg><svg class="clear"><use href="#beach-spot"/></svg><svg class="clear"><use href="#beach-spot"/></svg><svg class="clear"><use href="#beach-spot"/></svg>
    <!-- row 8 -->
    <svg class="clear"><use href="#beach-spot"/></svg><svg class="clear"><use href="#beach-spot"/></svg><svg class="clear"><use href="#beach-spot"/></svg><svg class="cancer"><use href="#beach-spot"/></svg><svg class="clear"><use href="#beach-spot"/></svg><svg class="clear"><use href="#beach-spot"/></svg><svg class="clear"><use href="#beach-spot"/></svg><svg class="cancer"><use href="#beach-spot"/></svg><svg class="clear"><use href="#beach-spot"/></svg><svg class="clear"><use href="#beach-spot"/></svg>
    <!-- row 9 -->
    <svg class="cancer"><use href="#beach-spot"/></svg><svg class="clear"><use href="#beach-spot"/></svg><svg class="clear"><use href="#beach-spot"/></svg><svg class="clear"><use href="#beach-spot"/></svg><svg class="clear"><use href="#beach-spot"/></svg><svg class="cancer"><use href="#beach-spot"/></svg><svg class="clear"><use href="#beach-spot"/></svg><svg class="clear"><use href="#beach-spot"/></svg><svg class="melanoma"><use href="#beach-spot"/></svg><svg class="clear"><use href="#beach-spot"/></svg>
    <!-- row 10 -->
    <svg class="clear"><use href="#beach-spot"/></svg><svg class="clear"><use href="#beach-spot"/></svg><svg class="cancer"><use href="#beach-spot"/></svg><svg class="clear"><use href="#beach-spot"/></svg><svg class="clear"><use href="#beach-spot"/></svg><svg class="clear"><use href="#beach-spot"/></svg><svg class="clear"><use href="#beach-spot"/></svg><svg class="clear"><use href="#beach-spot"/></svg><svg class="cancer"><use href="#beach-spot"/></svg><svg class="clear"><use href="#beach-spot"/></svg>
  </div>

  <ul class="legend">
    <li class="clear"><svg class="clear" aria-hidden="true"><use href="#beach-spot"/></svg>NO SKIN CANCER</li>
    <li class="cancer"><svg class="cancer" aria-hidden="true"><use href="#beach-spot"/></svg>SKIN CANCER</li>
    <li class="melanoma"><svg class="melanoma" aria-hidden="true"><use href="#beach-spot"/></svg>MELANOMA</li>
  </ul>

  <h2 class="prevent">What can you do to prevent skin cancer?</h2>
  <p class="more">...</p>
</main>
</body>
</html>
```